custom sticker for off the shelf postage packaging

Looking for a custom sticker to wrap around a postage box for gift hampers. Want to avoid custom printing onto the box, and so would like to glam up with a custom sticker. The design needs to be suitable for printing onto a paper sticker (rather than a vinyl sticker) so that the entire box is recyclable. Current marketing material and logo will be provided to the successful applicant. The gift hampers are filled with hand made goodies from places we can't travel to due to Covid. Brand is called TOVA and it stands for Tied With Sunshine.

Target Market(s)

Must appear to people who buy stuff on instagram

Industry/Entity Type

Gift Shop

Font styles to use
Other font styles liked:
• syncopate-regular

Requirements
Must have
• Must be eye catching and convey a sense of luxury. The recipient of the box is not the buyer, and won't be familiar with the website, or the brand. So this is a first impression. Draft website can be provided upon request.

Current branding is:
"bg":"#F6E7DC",
"font":"#2B1200",
"icon-gradient-0":"#792300",
"icon-gradient-1":"#F37000",
"slogan":"#3f2614"}
Nice to have
• Sticker should wrap around the box and cover the opening flap for postage security. The box is 310mm x 225mm x 102mm (length x width x height). Thinking that the sticker should be 225mm x 102 x 102mm *so the crease of the sticker should line up with the box. Text should be logo + text down the side "A gift of sunshine"

```html
<!DOCTYPE html>
<html lang="en">
<head>
<meta charset="UTF-8">
<title>TOVA – Box Wrap Sticker</title>
<link rel="stylesheet" href="https://fonts.googleapis.com/css2?family=Montserrat:wght@300;400&display=swap">
<style>
  :root {
    --stage: #000000;
    --paper: #ffffff;
    --ink: #231f20;
    --ribbon-dark: #792300;
    --ribbon-light: #F37000;
    --bow-deep: #c8000a;
    --bow-bright: #ff3b2a;
    --brand-name: #a83a05;
  }
  * { margin: 0; padding: 0; box-sizing: border-box; }
  html, body {
    width: 1200px;
    height: 720px;
    overflow: hidden;
    background: var(--stage);
  }
  .canvas {
    position: relative;
    width: 1200px;
    height: 720px;
    background: var(--stage);
  }
  .sticker {
    position: absolute;
    left: 280px;
    top: 70px;
    width: 640px;
    height: 580px;
    background: var(--paper);
    overflow: hidden;
  }
  .wordmark {
    position: absolute;
    left: 0;
    right: 0;
    top: 59px;
    text-align: center;
    font-family: "Montserrat", sans-serif;
    font-weight: 400;
    font-size: 134px;
    line-height: 1;
    letter-spacing: 0;
    color: var(--ink);
  }
  .ribbon {
    position: absolute;
    left: 0;
    top: 280px;
    width: 100%;
    height: 20px;
    background: linear-gradient(90deg, var(--ribbon-dark), var(--ribbon-light));
  }
  .bow {
    position: absolute;
    left: 240px;
    top: 213px;
    width: 162px;
    height: 166px;
    border-radius: 50% 50% 46% 46%;
    background: radial-gradient(circle at 45% 45%, var(--bow-bright) 0%, var(--bow-deep) 55%, rgba(200,0,10,0) 72%);
  }
  .brand-name {
    position: absolute;
    left: 327px;
    width: 80px;
    top: 442px;
    text-align: center;
    font-family: "Montserrat", sans-serif;
    font-weight: 300;
    font-size: 18px;
    line-height: 24px;
    letter-spacing: 2px;
    color: var(--brand-name);
  }
  .slogan {
    position: absolute;
    left: 0;
    right: 0;
    top: 470px;
    text-align: center;
    font-family: "Montserrat", sans-serif;
    font-weight: 300;
    font-size: 29px;
    line-height: 40px;
    color: var(--ink);
  }
</style>
</head>
<body>
  <main class="canvas">
    <section class="sticker">
      <h1 class="wordmark">TOVA</h1>
      <div class="ribbon"></div>
      <div class="bow" role="img" aria-label="Red satin gift bow tied over the ribbon"></div>
      <div class="brand-name">TOVA</div>
      <p class="slogan">A gift of sunshine</p>
    </section>
  </main>
</body>
</html>
```